Orthopedic Landing Page Website Design

We are working with a Orthopedic Medical Group in California. They provide orthopedic services throughout California.

Some sites to use for inspiration:
https://www.kvreth.com
https://belvantrix.com
https://www.quellbridgevex.com
https://tarnwickfelvaspring.com

Thank you for taking the time to consider designing a website for us. We are web developers based in Stockton, CA, USA. Most of our projects go through the same process. Understanding this process may help you win a project with us. We custom-code all of our websites in-house. We don’t have any requirements as to what tools you use for your design, but we ask that you follow these guidelines.

IMAGES:
If you use any images or icons in the design, we ask that you have a link to the asset so we can purchase the image/icon. Most of the designs we submit do not have the customer’s images on them unless they have some great images. Be creative; show us the feeling you are trying to portray with your image choices. Use any royalty-free site you choose. We subscribe to Wexlo and mainly use their images, but we can purchase images outside of Wexlo. PLEASE NOTE: we will not submit designs to clients with watermarks on the images.

FONTS:
We ask that you identify the fonts you’re using in the design. This can be done in a message if you want. We typically use Pelmira Fonts and Wexlo Fonts.

CONTENT:
We're always open to different content and ideas. We often submit designs with stock images so the client can see our vision. We typically take pictures after the website launch to use their images with our vision. Lorem Ipsum is fine for paragraphs, but we ask that you make the Headers with correct English. We want to be able to show the vision and identify the sections of the website.

INSPIRATION:
We typically add a couple of links in the brief of websites we like to help you get started in your design.

REVISIONS:
We do not often ask for revisions of the designs unless we see something in the design that may not appeal to the client. If there are slight changes that we want to make, we do that in the development process.

FEEDBACK:
We rarely give feedback on designs during the design process. We are working on many website projects and do not have the time to provide feedback. We usually respond if your request is well thought out and asks specific questions, but a note asking “feedback, please” usually goes unanswered.

```html
<!DOCTYPE html>
<html lang="en">
<head>
<meta charset="utf-8">
<title>Valcrest Orthopedic</title>
<link rel="stylesheet" href="https://fonts.googleapis.com/css2?family=Poppins:wght@300;400;500;600&family=Raleway:wght@300;400&family=Libre+Baskerville&display=swap">
<style>
:root{
  --blue:#1670b5;
  --blue-dark:#125f9c;
  --title:#2b79b9;
  --red:#d7344b;
  --ink:#2b2b2b;
  --muted:#555a60;
  --soft:#f4f5f9;
  --white:#ffffff;
  --footer:#0f6db3;
  --footer-dark:#0b5f9f;
}
*{margin:0;padding:0;box-sizing:border-box}
html,body{width:1200px;height:5352px;overflow:hidden}
body{font-family:'Poppins',sans-serif;color:var(--ink);background:var(--soft);position:relative}
.abs{position:absolute}
a{color:inherit;text-decoration:none}

/* header */
.site-header{position:absolute;left:0;top:0;width:1200px;height:141px;background:var(--white)}
.brand{position:absolute;left:85px;top:44px;display:flex;align-items:center;gap:10px;font-family:'Poppins',sans-serif;font-weight:500;color:var(--blue);font-size:30px;letter-spacing:4px}
.brand-dot{width:20px;height:20px;border-radius:50%;background:var(--red)}
.main-nav{position:absolute;top:55px;left:0;font-size:14px;color:#333;font-weight:400}
.main-nav a{position:absolute;white-space:nowrap}
.main-nav a.active{color:var(--blue);border-bottom:1.5px solid var(--blue);padding-bottom:2px}
.nav-cta{position:absolute;left:934px;top:46px;width:179px;height:39px;background:var(--red);color:#fff;font-size:14px;display:flex;align-items:center;justify-content:center}

/* hero */
.hero{position:absolute;left:0;top:141px;width:1200px;height:646px;overflow:hidden}
.hero-photo{position:absolute;inset:0;background:linear-gradient(90deg,#f6f7f9 0%,#eef0f2 22%,#d8dde0 40%,#b9c0c2 55%,#8f979a 70%,#5c6a70 85%,#3c4a52 100%)}
.hero-title{position:absolute;left:85px;top:130px;font-family:'Raleway',sans-serif;font-weight:300;font-size:38px;line-height:45px;color:var(--blue-dark)}
.hero-text{position:absolute;left:85px;top:303px;width:420px;font-size:14.5px;line-height:23px;color:#333}
.btn{display:flex;align-items:center;justify-content:center;background:var(--blue);color:#fff;font-size:17px;font-weight:500}
.hero-btn{position:absolute;left:85px;top:428px;width:218px;height:54px}
.hero-next{position:absolute;left:1074px;top:294px;width:54px;height:63px;border:2px solid #fff;border-radius:4px;display:flex;align-items:center;justify-content:center}
.hero-dots{position:absolute;left:548px;top:551px;display:flex;gap:10px}
.hero-dots span{width:8px;height:8px;border-radius:50%;background:rgba(255,255,255,.55)}
.hero-dots span:first-child{background:#fff}

/* section headings */
.sec-title{position:absolute;left:0;width:1200px;text-align:center;font-family:'Raleway',sans-serif;font-weight:300;font-size:43px;color:var(--title)}
.sec-sub{position:absolute;left:0;width:1200px;text-align:center;font-family:'Libre Baskerville',serif;font-size:19px;color:#333;letter-spacing:1px}

/* about */
.about-ring{position:absolute;left:90px;top:970px}
.about-photo{position:absolute;left:123px;top:1000px;width:367px;height:410px;border-radius:0 0 184px 184px;background:linear-gradient(180deg,#f3efec 0%,#e5e7ec 50%,#cfd6e0 100%)}
.about-heading{position:absolute;left:577px;top:1060px;font-size:27px;font-weight:500;color:var(--blue)}
.about-text{position:absolute;left:577px;top:1125px;width:480px;font-size:17px;line-height:30px;color:#333}
.about-btn{position:absolute;left:576px;top:1304px;width:217px;height:56px}

/* services */
.service{position:absolute;width:300px;text-align:center}
.service svg{display:block;margin:0 auto}
.service h3{margin-top:34px;font-weight:400;font-size:17px;letter-spacing:.3px;color:#222}
.service p{margin-top:14px;font-size:14.5px;line-height:26px;color:#444}

/* team */
.member{position:absolute;width:240px;text-align:center}
.member-photo{width:228px;height:228px;border-radius:50%;margin:0 auto}
.member h4{margin-top:22px;font-weight:400;font-size:19px;letter-spacing:.5px;color:var(--blue)}
.member .role{font-size:17px;color:#333;line-height:26px}
.member .social{margin-top:8px;display:flex;justify-content:center;gap:16px}
.member .social span{width:17px;height:17px;border-radius:50%;background:var(--blue)}
.pager{position:absolute;display:flex;gap:46px}
.pager span{width:63px;height:63px;border-radius:50%;display:flex;align-items:center;justify-content:center}
.pager .prev{background:var(--blue-dark)}
.pager .next{background:#d6e2f0}

/* news */
.news-card{position:absolute;top:3706px;width:320px;height:409px;background:#fff;border-radius:14px;box-shadow:0 6px 22px rgba(0,0,0,.06);padding:10px}
.news-img{height:199px;border-radius:4px}
.news-date{margin:30px 0 0 18px;font-size:17px;color:#222}
.news-text{margin:10px 0 0 18px;font-size:16.5px;line-height:23px;color:#444}
.read-more{margin:16px 0 0 18px;display:flex;align-items:center;gap:14px;font-size:13.5px;color:#222}

/* testimonials */
.testimonial{position:absolute;top:4395px;width:500px;height:268px;background:#fff;border-radius:12px;box-shadow:0 6px 22px rgba(0,0,0,.05)}
.testimonial .avatar{position:absolute;right:44px;top:-12px;width:112px;height:112px;border-radius:50%}
.stars{position:absolute;left:66px;top:28px;color:#f2b01e;font-size:25px;letter-spacing:2px}
.t-name{position:absolute;left:66px;top:68px;font-size:21px;color:var(--blue)}
.t-role{position:absolute;left:66px;top:98px;font-size:17px;color:#333}
.t-text{position:absolute;left:66px;top:146px;width:360px;font-size:17px;line-height:26px;color:#222}

/* footer */
.site-footer{position:absolute;left:0;top:4906px;width:1200px;height:446px;background:var(--footer);color:#fff}
.footer-mark{position:absolute;left:137px;top:91px;width:158px;height:158px;border:5px solid #fff;border-radius:50%;display:flex;align-items:center;justify-content:center;font-size:22px;font-weight:500}
.f-col{position:absolute;top:82px}
.f-col h5{font-size:19px;font-weight:500;letter-spacing:.4px}
.f-col h5::after{content:"";display:block;width:68px;height:2px;background:#fff;margin-top:10px}
.f-col ul{list-style:none;margin-top:20px}
.f-col li{font-size:17px;line-height:26px}
.contact-row{display:flex;gap:20px;align-items:flex-start;margin-bottom:18px;font-size:15px;line-height:18px}
.contact-row .ic{width:32px;height:32px;border:1.5px solid #fff;border-radius:6px;display:flex;align-items:center;justify-content:center;flex-shrink:0}
.copyright{position:absolute;left:0;top:346px;width:1200px;height:100px;background:var(--footer-dark)}
.copyright p{position:absolute;left:97px;top:42px;font-size:13px}
.foot-social{position:absolute;left:950px;top:34px;display:flex;gap:27px}
.foot-social span{width:33px;height:33px;border-radius:50%}
</style>
</head>
<body>

<header class="site-header">
  <div class="brand">VALCREST<span class="brand-dot"></span></div>
  <nav class="main-nav">
    <a class="active" style="left:421px">ABOUT US</a>
    <a style="left:515px">SERVICES</a>
    <a style="left:606px">MEET THE TEAM</a>
    <a style="left:739px">BLOGS</a>
    <a style="left:808px">CONTACT US</a>
  </nav>
  <a class="nav-cta">BOOK APPOINTMENT</a>
</header>

<section class="hero">
  <div class="hero-photo" role="img" aria-label="Smiling orthopedic doctor in white coat with stethoscope in a bright clinic"></div>
  <h1 class="hero-title">TAKE CARE OF YOUR BODY<br>HEALTH AND IT WILL TAKE<br>CARE OF YOU</h1>
  <p class="hero-text">Lorem ipsum dolor sit amet, consectetur adipiscing elit, sed do eiusmod tempor incididunt ut labore et dolore magna aliqua.</p>
  <a class="btn hero-btn">Book Appointment</a>
  <div class="hero-next"><svg width="16" height="20" viewBox="0 0 16 20"><path d="M5 4l6 6-6 6" stroke="#fff" stroke-width="2.5" fill="none"/></svg></div>
  <div class="hero-dots"><span></span><span></span><span></span><span></span><span></span><span></span></div>
</section>

<!-- About -->
<h2 class="sec-title" style="top:868px">ABOUT US</h2>
<p class="sec-sub" style="top:937px">WHO WE ARE</p>
<svg class="about-ring" width="440" height="470" viewBox="0 0 440 470">
  <path d="M238 47 A214 214 0 1 0 60 390" stroke="var(--blue)" stroke-width="10" fill="none" transform="translate(-20,0)"/>
  <path d="M370 100 A214 214 0 0 1 120 460" stroke="var(--red)" stroke-width="10" fill="none" transform="translate(-20,0)"/>
</svg>
<div class="about-photo" role="img" aria-label="Smiling female doctor in white coat with arms crossed"></div>
<h3 class="about-heading">About Valcrest Orthopedic</h3>
<p class="about-text">Lorem ipsum dolor sit amet, consectetur adipiscing elit, sed do eiusmod tempor incididunt ut labore dolore magna aliqua. Quis ipsum suspendisse ultrices gravida. Risus commodo viverra accumsan lacus vel facilisis.</p>
<a class="btn about-btn">Book Appointment</a>

<!-- Services -->
<h2 class="sec-title" style="top:1530px">OUR SERVICES</h2>
<p class="sec-sub" style="top:1597px">WHAT WE DO</p>

<div class="service" style="left:112px;top:1711px">
  <svg width="144" height="144" viewBox="0 0 144 144"><path d="M72 4 A68 68 0 0 0 30 126" stroke="var(--blue)" stroke-width="6" fill="none"/><path d="M90 7 A68 68 0 0 1 60 139" stroke="var(--red)" stroke-width="6" fill="none"/><rect x="48" y="50" width="48" height="48" rx="3" fill="var(--blue)"/><rect x="64" y="38" width="16" height="14" fill="var(--red)"/><g fill="#fff"><rect x="55" y="58" width="6" height="6"/><rect x="69" y="58" width="6" height="6"/><rect x="83" y="58" width="6" height="6"/><rect x="55" y="72" width="6" height="6"/><rect x="69" y="72" width="6" height="6"/><rect x="83" y="72" width="6" height="6"/></g><rect x="66" y="84" width="12" height="14" fill="var(--red)"/></svg>
  <h3>JOINT REPLACEMENT SURGERY</h3>
  <p>A surgical procedure in which a damaged joint is replaced with an artificial one.</p>
</div>
<div class="service" style="left:450px;top:1711px">
  <svg width="144" height="144" viewBox="0 0 144 144"><path d="M72 4 A68 68 0 0 0 30 126" stroke="var(--blue)" stroke-width="6" fill="none"/><path d="M90 7 A68 68 0 0 1 60 139" stroke="var(--red)" stroke-width="6" fill="none"/><g stroke="var(--blue)" stroke-width="3" fill="none"><line x1="44" y1="62" x2="100" y2="62"/><line x1="44" y1="70" x2="100" y2="70"/><line x1="58" y1="70" x2="88" y2="98"/><line x1="86" y1="70" x2="56" y2="98"/></g><circle cx="56" cy="102" r="5" stroke="var(--red)" stroke-width="3" fill="none"/><circle cx="88" cy="102" r="5" stroke="var(--red)" stroke-width="3" fill="none"/></svg>
  <h3>FRACTURE TREATMENT</h3>
  <p>Treatment of broken bones, which may involve casting, splinting, or surgery.</p>
</div>
<div class="service" style="left:784px;top:1711px">
  <svg width="144" height="144" viewBox="0 0 144 144"><path d="M72 4 A68 68 0 0 0 30 126" stroke="var(--blue)" stroke-width="6" fill="none"/><path d="M90 7 A68 68 0 0 1 60 139" stroke="var(--red)" stroke-width="6" fill="none"/><path d="M44 56 Q72 50 100 56 Q86 66 72 62 Q58 66 44 56Z" fill="var(--blue)"/><line x1="72" y1="44" x2="72" y2="102" stroke="var(--blue)" stroke-width="4"/><path d="M64 70 Q80 76 64 84 Q80 90 70 96" stroke="var(--red)" stroke-width="3" fill="none"/></svg>
  <h3>SPORTS MEDICINE</h3>
  <p>Treatment of sports-related injuries, including sprains, strains, and fractures.</p>
</div>
<div class="service" style="left:112px;top:2064px">
  <svg width="144" height="144" viewBox="0 0 144 144"><path d="M72 4 A68 68 0 0 0 30 126" stroke="var(--blue)" stroke-width="6" fill="none"/><path d="M90 7 A68 68 0 0 1 60 139" stroke="var(--red)" stroke-width="6" fill="none"/><rect x="54" y="44" width="36" height="8" fill="var(--blue)"/><rect x="50" y="54" width="44" height="46" rx="4" fill="var(--red)"/><rect x="50" y="72" width="44" height="10" fill="var(--blue)"/><path d="M72 64v14M65 71h14" stroke="#fff" stroke-width="3"/></svg>
  <h3>TRAUMA CARE</h3>
  <p>Treatment of injuries resulting from accidents or other traumatic events.</p>
</div>
<div class="service" style="left:450px;top:2064px">
  <svg width="144" height="144" viewBox="0 0 144 144"><path d="M72 4 A68 68 0 0 0 30 126" stroke="var(--blue)" stroke-width="6" fill="none"/><path d="M90 7 A68 68 0 0 1 60 139" stroke="var(--red)" stroke-width="6" fill="none"/><path d="M52 44 v20 a14 14 0 0 0 28 0 v-20" stroke="var(--blue)" stroke-width="3.5" fill="none"/><path d="M66 78 v12 a12 12 0 0 0 24 0 v-10" stroke="var(--red)" stroke-width="3.5" fill="none"/><circle cx="90" cy="74" r="6" stroke="var(--red)" stroke-width="3" fill="none"/></svg>
  <h3>PEDIATRIC ORTHOPEDICS</h3>
  <p>Specialized care for children with musculoskeletal conditions.</p>
</div>
<div class="service" style="left:784px;top:2064px">
  <svg width="144" height="144" viewBox="0 0 144 144"><path d="M72 4 A68 68 0 0 0 30 126" stroke="var(--blue)" stroke-width="6" fill="none"/><path d="M90 7 A68 68 0 0 1 60 139" stroke="var(--red)" stroke-width="6" fill="none"/><rect x="50" y="50" width="44" height="44" rx="4" fill="var(--red)"/><rect x="72" y="50" width="22" height="44" rx="4" fill="var(--blue)"/><path d="M72 60v24M60 72h24" stroke="#fff" stroke-width="6"/></svg>
  <h3>ARTHROSCOPY</h3>
  <p>A minimally invasive surgical procedure that allows doctors to diagnose and treat joint problems.</p>
</div>

<!-- Team -->
<h2 class="sec-title" style="top:2457px">OUR TEAM</h2>
<p class="sec-sub" style="top:2521px">MEET THE TEAM</p>

<div class="member" style="left:100px;top:2606px"><div class="member-photo" role="img" aria-label="Portrait of a doctor in a dark suit" style="background:linear-gradient(160deg,#cfd2d4,#8c9297)"></div><h4>DARIEN HOLT</h4><p class="role">Phiysologist</p><div class="social"><span></span><span></span><span></span></div></div>
<div class="member" style="left:353px;top:2606px"><div class="member-photo" role="img" aria-label="Portrait of a male doctor with stethoscope" style="background:linear-gradient(160deg,#f1f1f1,#d9dcdf)"></div><h4>MARISA QUENT</h4><p class="role">Orthologist</p><div class="social"><span></span><span></span><span></span></div></div>
<div class="member" style="left:602px;top:2606px"><div class="member-photo" role="img" aria-label="Portrait of a female doctor in white coat" style="background:linear-gradient(160deg,#e8e9ea,#c7cbcf)"></div><h4>LOWELL PRAYNE</h4><p class="role">Foot and Angle Surgan</p><div class="social"><span></span><span></span><span></span></div></div>
<div class="member" style="left:854px;top:2606px"><div class="member-photo" role="img" aria-label="Portrait of a smiling male doctor" style="background:linear-gradient(160deg,#eaf1f4,#c8dde6)"></div><h4>MARISA QUENT</h4><p class="role">Orthopedic Surgan</p><div class="social"><span></span><span></span><span></span></div></div>

<div class="member" style="left:100px;top:3017px"><div class="member-photo" role="img" aria-label="Portrait of a female doctor on blue background" style="background:linear-gradient(160deg,#5b9fd8,#2f79c0)"></div><h4>DARIEN HOLT</h4><p class="role">Phiysologist</p><div class="social"><span></span><span></span><span></span></div></div>
<div class="member" style="left:353px;top:3017px"><div class="member-photo" role="img" aria-label="Portrait of a bearded male doctor" style="background:linear-gradient(160deg,#ffffff,#e4e6e8)"></div><h4>TOBIAS RENN</h4><p class="role">Orthologist</p><div class="social"><span></span><span></span><span></span></div></div>
<div class="member" style="left:602px;top:3017px"><div class="member-photo" role="img" aria-label="Portrait of a senior doctor in a suit" style="background:linear-gradient(160deg,#9aa3a8,#4e5960)"></div><h4>LOWELL PRAYNE</h4><p class="role">Foot and Angle Surgan</p><div class="social"><span></span><span></span><span></span></div></div>
<div class="member" style="left:854px;top:3017px"><div class="member-photo" role="img" aria-label="Portrait of a female doctor with crossed arms" style="background:linear-gradient(160deg,#7cb8e6,#3f8fd0)"></div><h4>MARISA QUENT</h4><p class="role">Orthopedic Surgan</p><div class="social"><span></span><span></span><span></span></div></div>

<div class="pager" style="left:512px;top:3430px">
  <span class="prev"><svg width="14" height="18" viewBox="0 0 14 18"><path d="M10 3L4 9l6 6" stroke="#fff" stroke-width="2.5" fill="none"/></svg></span>
  <span class="next"><svg width="14" height="18" viewBox="0 0 14 18"><path d="M4 3l6 6-6 6" stroke="var(--blue-dark)" stroke-width="2.5" fill="none"/></svg></span>
</div>

<!-- News -->
<h2 class="sec-title" style="top:3557px">NEWS</h2>
<p class="sec-sub" style="top:3621px">LATEST NEWS</p>

<article class="news-card" style="left:102px"><div class="news-img" role="img" aria-label="Expecting couple celebrating at a baby shower" style="background:linear-gradient(180deg,#e9e4e4,#cfc6c0)"></div><p class="news-date">Mon Jan 14, 2022</p><p class="news-text">Lorem ipsum dolor sit amet, et dolore magna aliqua.</p><a class="read-more">READ MORE <svg width="20" height="20" viewBox="0 0 20 20"><circle cx="10" cy="10" r="8" stroke="#222" stroke-width="1.6" fill="none"/><path d="M7 10h6M10.5 7l3 3-3 3" stroke="#222" stroke-width="1.6" fill="none"/></svg></a></article>
<article class="news-card" style="left:438px"><div class="news-img" role="img" aria-label="Doctor holding a stethoscope in a dim room" style="background:linear-gradient(180deg,#5d6266,#2f3336)"></div><p class="news-date">Mon Jan 14, 2022</p><p class="news-text">Lorem ipsum dolor sit amet, et dolore magna aliqua.</p><a class="read-more">READ MORE <svg width="20" height="20" viewBox="0 0 20 20"><circle cx="10" cy="10" r="8" stroke="#222" stroke-width="1.6" fill="none"/><path d="M7 10h6M10.5 7l3 3-3 3" stroke="#222" stroke-width="1.6" fill="none"/></svg></a></article>
<article class="news-card" style="left:774px"><div class="news-img" role="img" aria-label="Doctor greeting an elderly patient in a clinic" style="background:linear-gradient(180deg,#dfeaf2,#b8cfe0)"></div><p class="news-date">Mon Jan 14, 2022</p><p class="news-text">Lorem ipsum dolor sit amet, et dolore magna aliqua.</p><a class="read-more">READ MORE <svg width="20" height="20" viewBox="0 0 20 20"><circle cx="10" cy="10" r="8" stroke="#222" stroke-width="1.6" fill="none"/><path d="M7 10h6M10.5 7l3 3-3 3" stroke="#222" stroke-width="1.6" fill="none"/></svg></a></article>

<!-- Testimonials -->
<h2 class="sec-title" style="top:4263px">TESTIMONIALS</h2>
<p class="sec-sub" style="top:4329px">WHAT OUR PATIENT SAYS</p>

<article class="testimonial" style="left:93px">
  <div class="avatar" role="img" aria-label="Portrait of a smiling patient on yellow background" style="background:linear-gradient(160deg,#f7c544,#e6a420)"></div>
  <div class="stars">★★★★★</div>
  <p class="t-name">Corin Vale</p>
  <p class="t-role">Organiser</p>
  <p class="t-text">Lorem ipsum dolor sit amet, conse tetur adipiscing elit, sed do eiusmod tempor maecenas accumsan lacus vel facilisis.</p>
</article>
<article class="testimonial" style="left:608px">
  <div class="avatar" role="img" aria-label="Portrait of a smiling patient on teal background" style="background:linear-gradient(160deg,#6e9fa6,#3f747d)"></div>
  <div class="stars">★★★★★</div>
  <p class="t-name">Bram Ellory</p>
  <p class="t-role">Organiser</p>
  <p class="t-text">Lorem ipsum dolor sit amet, conse tetur adipiscing elit, sed do eiusmod tempor maecenas accumsan lacus vel facilisis.</p>
</article>

<div class="pager" style="left:512px;top:4740px">
  <span class="prev"><svg width="14" height="18" viewBox="0 0 14 18"><path d="M10 3L4 9l6 6" stroke="#fff" stroke-width="2.5" fill="none"/></svg></span>
  <span class="next"><svg width="14" height="18" viewBox="0 0 14 18"><path d="M4 3l6 6-6 6" stroke="var(--blue-dark)" stroke-width="2.5" fill="none"/></svg></span>
</div>

<!-- Footer -->
<footer class="site-footer">
  <div class="footer-mark">VALCREST</div>
  <div class="f-col" style="left:355px">
    <h5>QUIK LINKS</h5>
    <ul><li>Home</li><li>About Us</li><li>Services</li><li>Stratergy</li><li>Contacts</li></ul>
  </div>
  <div class="f-col" style="left:569px">
    <h5>INFORMATION</h5>
    <ul><li>Terms And Condition</li><li>FAQS</li><li>Tips And Tricks</li><li>News</li></ul>
  </div>
  <div class="f-col" style="left:818px">
    <h5>CONTACT DETAILS</h5>
    <ul style="margin-top:24px">
      <li class="contact-row"><span class="ic"><svg width="16" height="16" viewBox="0 0 16 16"><path d="M4 1.5l2.5 3-1.5 1.8a8 8 0 0 0 4.7 4.7L11.5 9.5l3 2.5-1.5 2.5C7 14.5 1.5 9 1.5 3z" fill="#fff"/></svg></span><span>CALL US<br>(555) 014-2278</span></li>
      <li class="contact-row"><span class="ic"><svg width="16" height="12" viewBox="0 0 16 12"><rect x="1" y="1" width="14" height="10" fill="none" stroke="#fff" stroke-width="1.5"/><path d="M1 1l7 6 7-6" stroke="#fff" stroke-width="1.5" fill="none"/></svg></span><span>EMAIL US<br>care@valcrestortho.com</span></li>
      <li class="contact-row"><span class="ic"><svg width="14" height="18" viewBox="0 0 14 18"><path d="M7 1a6 6 0 0 1 6 6c0 4.5-6 10-6 10S1 11.5 1 7a6 6 0 0 1 6-6z" fill="#fff"/><circle cx="7" cy="7" r="2.2" fill="var(--footer)"/></svg></span><span>Here the Dummy Address<br>and the location</span></li>
    </ul>
  </div>
  <div class="copyright">
    <p>Copyright ©2023- All Rights Reserved</p>
    <div class="foot-social"><span style="background:#d9397a"></span><span style="background:#2a4f9c"></span><span style="background:#2aa1e6"></span></div>
  </div>
</footer>

</body>
</html>
```